Business Card Design

hello Guys,
We need a double sided business card. Would like a clean and modern look. Simple, clean, elegant.

Front:
Logo/Company name or Logo/Products
Back:
Contact details

You can go to our website for color scheme.

Information for the business cards are as follows:
Our logo (it is attached)
Products: Divisórias, Forros, Persianas, Pisos
The Company name is: Lumen Painéis
Name: Rodrigo Matheus Valente
Position: Diretor Comercial
Tel: 11 3917-4482 / 95827-6043 / ID: 48*17*26584
Email: contato@lumenpaineis.com.br
Web: www.lumenpaineis.com.br
Address: R: Otávio Brandão 83 – São Paulo – CEP: 04718-230

The card should be of 85mm x 55mm
The winner will deliver:

1) JPG, PNG, TIFF, PDF, Ai, EPS, PSD format files.
The work product will be an Illustrator or Photoshop file
Good luck and let me know if you have any other questions.

CMYK, 300 dpi, convert fonts into paths (vector paths)
set margins at least 4 mm away from the edges

Thanks

```html
<!DOCTYPE html>
<html lang="pt-BR">
<head>
<meta charset="utf-8">
<title>Lumen Painéis – Cartão de Visita</title>
<link href="https://fonts.googleapis.com/css2?family=Open+Sans:wght@400;600;700&display=swap" rel="stylesheet">
<style>
  :root {
    --orange: #f0883a;
    --orange-deep: #e8762a;
    --white: #ffffff;
    --ink: #5a5a5a;
    --ink-soft: #8a8a8a;
    --rule: #c9c9c9;
    --stripe: #6d6d6d;
    --backdrop: #e6e6e6;
  }
  * { box-sizing: border-box; margin: 0; padding: 0; }
  html, body { width: 1200px; height: 675px; overflow: hidden; }
  body {
    background: var(--backdrop);
    font-family: "Open Sans", sans-serif;
    position: relative;
  }
  .card {
    position: absolute;
    top: 170px;
    width: 520px;
    height: 336px;
    overflow: hidden;
    box-shadow: 0 2px 8px rgba(0,0,0,0.12);
  }
  /* Front */
  .card-front {
    left: 50px;
    background: linear-gradient(135deg, var(--orange) 0%, var(--orange-deep) 100%);
    color: var(--white);
  }
  .front-brand {
    position: absolute;
    left: 0; right: 0; top: 110px;
    display: flex; align-items: center; justify-content: center; gap: 14px;
  }
  .brand-dot {
    width: 22px; height: 22px; border-radius: 50%;
    background: var(--white);
  }
  .front-brand .brand-name {
    font-size: 40px; font-weight: 600; letter-spacing: 1px; color: var(--white);
  }
  .front-products {
    position: absolute; left: 0; right: 0; top: 206px;
    text-align: center; font-size: 15px; font-weight: 600; letter-spacing: 0.5px;
  }
  /* Back */
  .card-back {
    left: 630px;
    background: var(--white);
    color: var(--ink);
  }
  .back-brand {
    position: absolute; right: 40px; top: 50px;
    display: flex; align-items: center; gap: 10px;
  }
  .back-brand .brand-dot { background: var(--orange); width: 18px; height: 18px; }
  .back-brand .brand-name {
    font-size: 30px; font-weight: 600; color: var(--orange); letter-spacing: 0.5px;
  }
  .back-rule {
    position: absolute; left: 40px; right: 40px; top: 186px;
    height: 1px; background: var(--rule);
  }
  .contact {
    position: absolute; left: 40px; top: 196px;
  }
  .contact-name { font-size: 17px; font-weight: 700; color: var(--orange); }
  .contact-role { font-size: 12px; color: var(--ink-soft); margin: 2px 0 8px; }
  .contact-line {
    display: flex; align-items: center; gap: 8px;
    font-size: 12px; line-height: 18px; color: var(--ink);
  }
  .contact-line svg { width: 11px; height: 11px; fill: var(--orange); flex: none; }
  .address {
    position: absolute; right: 40px; top: 196px;
    text-align: right; font-size: 12px; line-height: 18px; color: var(--ink);
  }
  .back-band { position: absolute; left: 0; bottom: 0; width: 520px; height: 90px; }
  .website {
    position: absolute; right: 40px; bottom: 48px;
    font-size: 12px; color: var(--white); letter-spacing: 0.3px;
  }
</style>
</head>
<body>

  <section class="card card-front">
    <div class="front-brand">
      <span class="brand-dot"></span>
      <span class="brand-name">Lumen Painéis</span>
    </div>
    <p class="front-products">Divisórias | Forros | Persianas | Pisos</p>
  </section>

  <section class="card card-back">
    <div class="back-brand">
      <span class="brand-dot"></span>
      <span class="brand-name">Lumen Painéis</span>
    </div>

    <div class="back-rule"></div>

    <div class="contact">
      <p class="contact-name">Rodrigo Matheus Valente</p>
      <p class="contact-role">Diretor Comercial</p>
      <p class="contact-line">
        <svg viewBox="0 0 12 12"><path d="M1 3c0-1 1-2 2-2h6c1 0 2 1 2 2v1H8V3H4v1H1zM2 5h8l1 6H1z"/></svg>
        11 3917-4482 / 95827-6043
      </p>
      <p class="contact-line">
        <svg viewBox="0 0 12 12"><rect x="3" y="0" width="6" height="12" rx="1"/></svg>
        ID: 48*17*26584
      </p>
      <p class="contact-line">
        <svg viewBox="0 0 12 12"><path d="M2 1l3 0 1 3-2 1c1 2 2 3 3 3l1-2 3 1 0 3c-6 0-9-3-9-9z"/></svg>
        contato@lumenpaineis.com.br
      </p>
      <p class="contact-line">
        <svg viewBox="0 0 12 12"><path d="M0 2h12v8H0zM1 3l5 4 5-4z" fill-rule="evenodd"/></svg>
        contato@lumenpaineis.com.br
      </p>
    </div>

    <div class="address">
      <p>R: Otávio Brandão 83 – São Paulo</p>
      <p>CEP: 04718-230</p>
    </div>

    <svg class="back-band" viewBox="0 0 520 90" preserveAspectRatio="none" aria-hidden="true">
      <path d="M0 78 L250 78 C275 78 280 42 305 42 L520 42 L520 48 L308 48 C284 48 278 84 250 84 L0 84 Z" fill="var(--stripe)"/>
      <path d="M0 84 L250 84 C278 84 284 48 308 48 L520 48 L520 90 L0 90 Z" fill="var(--orange)"/>
    </svg>
    <p class="website">www.lumenpaineis.com.br</p>
  </section>

</body>
</html>
```